MARLOW CREST WINE LABEL DESIGN PROJECT

We need an elegant wine label design for our new range of wine. We need 3 labels for the range

2015 MARLOW CREST SHIRAZ
2015 MARLOW CREST CABERNET SAUVIGNON
2015 MARLOW CREST CABERNET SHIRAZ

The Size is nominated at 120mm High x 90mm Wide (Front and Back) but we are open to creative expression even if size differs

We are open to any style of label and designer can work on their strengths. it can be modern/classic/old fashion etc

I have attached the marlow crest logo ( the 2 olives) and a set up called wine mandatories which is in no way a design direction just the mandatory info that needs to appear on labels. The wine mandatories is just the information that needs to go on the label it has nothing to do with the design. DO not make designs based on this at all. These labels are for red wine not olive oil.

I have also attached some of the companies current olive oil labels ( TORQUALE AND WANDELLA AND MARLOW CREST so you can see other labels and how this wine product will sit in gift baskets.

Thanks
Tomasz.

Reason: Hello Friends We have decided to extend the deadline to enable more submissions. Many of the designs submitted have images of olives and look like olive oil product. We only need the olive logo to be shown on the label but the rest of the design should be a classic simple red wine label. It is not olive oil or olive product - it is red wine. Please keep simple and stylish Thanks Tomasz

Target Market(s)

35-65

Font styles to use
Serif

Requirements
Must have
• AS per brief
Nice to have
• as per brief
Should not have
• as per brief

```html
<!DOCTYPE html>
<html lang="en">
<head>
<meta charset="utf-8">
<title>Marlow Crest Shiraz 2015 – Wine Label</title>
<link href="https://fonts.googleapis.com/css2?family=Montserrat:wght@700&family=Oswald:wght@400&family=Parisienne&family=Roboto+Condensed:wght@700&display=swap" rel="stylesheet">
<style>
  :root {
    --cream: #f8dc9a;
    --frame-violet: #5a3f8a;
    --olive-panel: #b3a035;
    --plum: #2f1f2c;
    --ink: #141210;
    --amber: #f4bd3c;
    --rust: #b95b16;
    --orange-edge: #e8852a;
    --white: #ffffff;
    --ribbon: #6e8438;
    --ribbon-light: #7f9645;
    --ribbon-fold: #8a6a2c;
    --script-cream: #f6cf8a;
  }
  html, body {
    margin: 0;
    padding: 0;
    overflow: hidden;
  }
  .label {
    position: relative;
    width: 1200px;
    height: 2667px;
    background: var(--cream);
    overflow: hidden;
  }
  .label__frame {
    position: absolute;
    inset: 0;
  }
  .label__panel {
    position: absolute;
    left: 94px;
    top: 85px;
    width: 1012px;
    height: 2488px;
    background: var(--olive-panel);
  }
  .brand-mark {
    position: absolute;
    left: 530px;
    top: 250px;
    width: 150px;
    height: 150px;
    border-radius: 50%;
    background: var(--plum);
  }
  .brand-name {
    position: absolute;
    left: 94px;
    width: 1012px;
    top: 700px;
    margin: 0;
    text-align: center;
    font-family: "Montserrat", sans-serif;
    font-weight: 700;
    font-size: 60px;
    letter-spacing: 0.2em;
    color: var(--ink);
  }
  .brand-tagline {
    position: absolute;
    left: 94px;
    width: 1012px;
    top: 822px;
    margin: 0;
    text-align: center;
    font-family: "Roboto Condensed", sans-serif;
    font-weight: 700;
    font-size: 42px;
    letter-spacing: 0.16em;
    color: var(--ink);
  }
  .feature {
    position: absolute;
    left: 143px;
    top: 1040px;
    width: 924px;
    height: 1189px;
    border-radius: 130px;
    background: var(--amber);
    overflow: hidden;
  }
  .feature__seal {
    position: absolute;
    left: 459px;
    top: 966px;
    width: 294px;
    height: 294px;
    border-radius: 50%;
    background: var(--rust);
    z-index: 2;
  }
  .feature__title {
    position: absolute;
    left: 0;
    width: 100%;
    top: 235px;
    margin: 0;
    text-align: center;
    font-family: "Oswald", sans-serif;
    font-weight: 400;
    font-size: 124px;
    letter-spacing: 0.06em;
    line-height: 1;
    color: var(--white);
    -webkit-text-stroke: 3px var(--orange-edge);
  }
  .feature__script {
    position: absolute;
    left: 0;
    width: 100%;
    top: 330px;
    margin: 0;
    text-align: center;
    font-family: "Parisienne", cursive;
    font-size: 330px;
    line-height: 1.1;
    color: var(--white);
  }
  .feature__landscape {
    position: absolute;
    left: 0;
    right: 0;
    bottom: 0;
    height: 455px;
    background: linear-gradient(to bottom,
      var(--amber) 0%,
      #fbe3a8 18%,
      #fff6df 26%,
      #c9962f 34%,
      #a87a22 55%,
      #8c6418 100%);
  }
  .varietal {
    position: absolute;
    left: 0;
    top: 0;
    width: 1200px;
    height: 2667px;
  }
  .varietal__vintage,
  .varietal__grape {
    position: absolute;
    left: 0;
    width: 1200px;
    margin: 0;
    text-align: center;
    font-family: "Roboto Condensed", sans-serif;
    font-weight: 700;
    color: var(--white);
    line-height: 1;
  }
  .varietal__vintage {
    top: 2272px;
    font-size: 52px;
    letter-spacing: 0.04em;
  }
  .varietal__name {
    position: absolute;
    left: 0;
    width: 1200px;
    top: 2298px;
    margin: 0;
    text-align: center;
    font-family: "Parisienne", cursive;
    font-size: 104px;
    line-height: 1.2;
    color: var(--script-cream);
  }
  .varietal__grape {
    top: 2418px;
    font-size: 50px;
    letter-spacing: 0.04em;
  }
  .mandatory {
    position: absolute;
    top: 2510px;
    margin: 0;
    font-family: "Roboto Condensed", sans-serif;
    font-weight: 700;
    font-size: 34px;
    color: var(--white);
  }
  .mandatory--alcohol { left: 301px; }
  .mandatory--volume { right: 290px; }
</style>
</head>
<body>
<main class="label">
  <svg class="label__frame" width="1200" height="2667" viewBox="0 0 1200 2667" aria-hidden="true">
    <path d="M84 28 L1116 28 A56 56 0 0 0 1172 84 L1172 2583 A56 56 0 0 0 1116 2639 L84 2639 A56 56 0 0 0 28 2583 L28 84 A56 56 0 0 0 84 28 Z" fill="none" stroke="var(--frame-violet)" stroke-width="2"/>
    <path d="M84 40 L1116 40 A44 44 0 0 0 1160 84 L1160 2583 A44 44 0 0 0 1116 2627 L84 2627 A44 44 0 0 0 40 2583 L40 84 A44 44 0 0 0 84 40 Z" fill="none" stroke="var(--frame-violet)" stroke-width="2"/>
  </svg>

  <div class="label__panel"></div>

  <div class="brand-mark" aria-hidden="true"></div>
  <h1 class="brand-name">THE MARLOW CREST</h1>
  <p class="brand-tagline">PREMIUM AUSTRALIAN WINE</p>

  <div class="feature__seal" aria-hidden="true"></div>

  <section class="feature">
    <h2 class="feature__title">THE MARLOW</h2>
    <p class="feature__script">crest</p>
    <div class="feature__landscape" role="img" aria-label="Golden-toned photograph of orchard rows stretching to the horizon"></div>
  </section>

  <svg class="varietal" width="1200" height="2667" viewBox="0 0 1200 2667" aria-hidden="true">
    <polygon points="170,2300 270,2300 270,2545 155,2545 195,2425" fill="var(--ribbon)"/>
    <polygon points="1030,2300 930,2300 930,2545 1045,2545 1005,2425" fill="var(--ribbon)"/>
    <polygon points="225,2470 270,2470 270,2545" fill="var(--ribbon-fold)"/>
    <polygon points="975,2470 930,2470 930,2545" fill="var(--ribbon-fold)"/>
    <rect x="225" y="2252" width="750" height="218" fill="var(--ribbon)"/>
    <polygon points="225,2420 975,2262 975,2330 420,2420" fill="var(--ribbon-light)"/>
  </svg>
  <p class="varietal__vintage">2015</p>
  <p class="varietal__name">marlow crest</p>
  <p class="varietal__grape">SHIRAZ</p>

  <p class="mandatory mandatory--alcohol">14.5% ALC/VOL</p>
  <p class="mandatory mandatory--volume">750 ML</p>
</main>
</body>
</html>
```